Innovative Consulting Firm Needs New Business Cards and Stationary

Our Innovative Consulting Firm, Larkfield Consulting, is in need of new business cards and stationary designs. We want two-sided cards that incorporate our logo, which is attached. We are looking for something not too formal, but is professional and slick.

Card should have the following information:
Name (ex. Tom Bradley)
Title (ex. Manager)
Address (ex. 24680 Cedar Lane)
Address 2 (ex. Suite 100)
City
State
Zip Code
Mobile
Email

The card should also have our website: www.larkfieldconsulting.example

Industry/Entity Type

Management Consulting

Contact Information for Business Card

Name (ex. Tom Bradley)
Title (ex. Manager)
Address 2 (ex. Suite 100)
City
State
Zip Code
Mobile
Email

Font styles to use
Sans Serif

Requirements
Must have
• The colors on the card must match the colors in the logo. The exact color codes are attached in a pdf.
Nice to have
• The Company's Tagline is "Focused on your Future". This might be nice to incorporate, but not necessary.

```html
<!DOCTYPE html>
<html lang="en">
<head>
<meta charset="utf-8">
<title>Larkfield Consulting – Business Cards</title>
<link href="https://fonts.googleapis.com/css2?family=Open+Sans:wght@400;600;700&display=swap" rel="stylesheet">
<style>
  :root {
    --backdrop: #2b2b2b;
    --card: #151515;
    --brand-blue: #2f5f93;
    --brand-gold: #f2b01e;
    --text-light: #e6e6e6;
    --text-muted: #bdbdbd;
  }
  * { box-sizing: border-box; margin: 0; padding: 0; }
  html, body {
    width: 1200px; height: 900px; overflow: hidden;
    background: var(--backdrop);
    font-family: "Open Sans", Arial, sans-serif;
  }
  .canvas {
    position: relative; width: 1200px; height: 900px;
    display: flex; align-items: center; justify-content: center; gap: 50px;
  }
  .card {
    position: relative; width: 525px; height: 300px;
    background: var(--card); border-radius: 22px;
    box-shadow: 0 10px 30px rgba(0,0,0,.45);
  }
  .wordmark {
    display: flex; align-items: center; gap: 10px;
    color: var(--brand-blue); font-weight: 600; white-space: nowrap;
  }
  .wordmark-dot {
    width: 14px; height: 14px; border-radius: 50%;
    background: var(--brand-gold); flex: none;
  }
  /* Front */
  .card-front .wordmark {
    position: absolute; left: 32px; top: 104px; font-size: 21px;
  }
  .contact {
    position: absolute; left: 292px; top: 88px; color: var(--text-light);
    font-size: 13.5px; line-height: 1.45;
  }
  .person-name { font-size: 17px; font-weight: 700; line-height: 1.2; }
  .person-name .first { color: var(--brand-gold); }
  .person-name .last { color: var(--brand-blue); }
  .person-title { font-size: 12.5px; color: var(--text-muted); margin-bottom: 10px; }
  .address { margin-bottom: 10px; }
  .contact-list { list-style: none; }
  .contact-list li { display: flex; align-items: center; gap: 8px; }
  .contact-list svg { width: 11px; height: 11px; flex: none; }
  /* Back */
  .card-back .wordmark {
    position: absolute; left: 0; right: 0; top: 108px;
    justify-content: center; font-size: 30px;
  }
  .card-back .wordmark-dot { width: 18px; height: 18px; }
  .back-website {
    position: absolute; left: 0; right: 0; top: 218px; text-align: center;
    color: var(--brand-gold); font-size: 13px; font-weight: 700;
  }
</style>
</head>
<body>
<main class="canvas">
  <section class="card card-front">
    <div class="wordmark"><span class="wordmark-dot"></span>Larkfield Consulting</div>
    <div class="contact">
      <p class="person-name"><span class="first">Tom</span> <span class="last">Bradley</span></p>
      <p class="person-title">Manager</p>
      <p class="address">24680 Cedar Lane, Suite 100,<br>City State, Zip Code</p>
      <ul class="contact-list">
        <li>
          <svg viewBox="0 0 12 12"><path fill="var(--brand-gold)" d="M2.5 1 4.3 1 5 3.6 3.8 4.6c.6 1.4 1.8 2.6 3.6 3.6L8.4 7 11 7.7 11 9.5c0 .8-.7 1.5-1.5 1.5C5 11 1 7 1 2.5 1 1.7 1.7 1 2.5 1z"/></svg>
          (044)-555-0142
        </li>
        <li>
          <svg viewBox="0 0 12 12"><rect x="1" y="2.5" width="10" height="7" rx="1" fill="var(--brand-gold)"/><path d="M1.5 3 6 6.5 10.5 3" fill="none" stroke="var(--card)" stroke-width="1"/></svg>
          info@larkfield.example
        </li>
        <li>
          <svg viewBox="0 0 12 12"><circle cx="6" cy="6" r="5" fill="var(--brand-gold)"/><path d="M1.5 6h9M6 1c-2 2.5-2 7.5 0 10M6 1c2 2.5 2 7.5 0 10" fill="none" stroke="var(--card)" stroke-width=".8"/></svg>
          www.larkfieldconsulting.example
        </li>
      </ul>
    </div>
  </section>

  <section class="card card-back">
    <div class="wordmark"><span class="wordmark-dot"></span>Larkfield Consulting</div>
    <p class="back-website">www.larkfieldconsulting.example</p>
  </section>
</main>
</body>
</html>
```